Icons/images for company values

We have five company values, we have a new logo and a new look. I would like drawn images for each value that are in keeping with our look and feel.

Target Market(s)

internal/staff

Industry/Entity Type

media compliance

Requirements
Must have
• colours aligned with logo.

```html
<!DOCTYPE html>
<html lang="en">
<head>
<meta charset="utf-8">
<title>Company Values 2023</title>
<link rel="stylesheet" href="https://fonts.googleapis.com/css2?family=Poppins:wght@300;400&family=Rubik:wght@500;600;700&display=swap">
<style>
  :root {
    --ink: #111;
    --body: #1d1d1d;
    --v1: #0d5d7b;
    --v2: #1383c3;
    --v3: #3ec2b3;
    --v4: #8fe07c;
    --v5: #f6d945;
    --card-top: #f1f1f1;
    --card-bottom: #fbfbfb;
  }
  * { box-sizing: border-box; margin: 0; padding: 0; }
  html, body { width: 1200px; height: 893px; overflow: hidden; background: #fff; }
  .canvas { position: relative; width: 1200px; height: 893px; font-family: "Poppins", sans-serif; color: var(--body); }

  .icon-row { position: absolute; top: 40px; left: 0; width: 1200px; height: 64px; }
  .icon-slot {
    position: absolute; width: 58px; height: 58px; border-radius: 50%;
    background: linear-gradient(135deg, var(--v1), var(--v3) 55%, var(--v5));
    opacity: .85;
  }
  .rule {
    position: absolute; top: 117px; left: 0; width: 1200px; height: 1px;
    background: linear-gradient(90deg, var(--v1), var(--v2) 35%, var(--v3) 60%, var(--v4) 80%, var(--v5));
  }

  .brand {
    position: absolute; left: 156px; top: 222px;
    font-family: "Poppins", sans-serif; font-weight: 400; font-size: 27px;
    letter-spacing: 12px; color: var(--v2);
  }

  .connectors { position: absolute; left: 0; top: 0; }

  .values-box {
    position: absolute; left: 91px; top: 386px; width: 239px; height: 238px;
    background: linear-gradient(180deg, rgba(240,240,240,.92), rgba(250,250,250,.92));
    box-shadow: 0 4px 14px rgba(0,0,0,.08);
  }
  .frame-top { position: absolute; left: 229px; top: 384px; width: 102px; height: 47px;
    border-top: 3px solid; border-right: 3px solid;
    border-image: linear-gradient(90deg, var(--v4), var(--v5)) 1; }
  .frame-bottom { position: absolute; left: 89px; top: 578px; width: 103px; height: 48px;
    border-left: 3px solid var(--v1); border-bottom: 3px solid var(--v2); }
  .values-title { position: absolute; left: 148px; top: 458px; font-family: "Poppins", sans-serif;
    font-weight: 400; font-size: 36px; line-height: 1; color: var(--ink); letter-spacing: -.5px; }
  .values-year { position: absolute; left: 147px; top: 492px; font-family: "Rubik", sans-serif;
    font-weight: 700; font-size: 52px; line-height: 1;
    background: linear-gradient(90deg, var(--v1), var(--v2) 30%, var(--v3) 55%, var(--v4) 75%, var(--v5));
    -webkit-background-clip: text; background-clip: text; color: transparent; }
  .year-dashes { position: absolute; left: 148px; top: 546px; display: flex; gap: 4px; }
  .year-dashes span { width: 22px; height: 3px; }

  .value-card {
    position: absolute; left: 493px; width: 604px; height: 118px;
    background: linear-gradient(180deg, var(--card-top), var(--card-bottom));
    box-shadow: 0 1px 4px rgba(0,0,0,.08);
    display: flex; align-items: center;
  }
  .value-icon {
    position: absolute; left: 41px; top: 32px; width: 54px; height: 54px; border-radius: 50%;
    opacity: .85;
  }
  .value-text { position: absolute; left: 130px; right: 20px; }
  .value-title { font-family: "Rubik", sans-serif; font-weight: 600; font-size: 18px;
    line-height: 22px; text-transform: uppercase; margin-bottom: 4px; }
  .value-body { font-size: 14.5px; line-height: 17px; font-weight: 400; }

  .c1 { top: 191px; } .c1 .value-title { color: var(--v1); } .c1 .value-icon { background: linear-gradient(135deg, var(--v1), var(--v2)); }
  .c2 { top: 319px; } .c2 .value-title { color: var(--v2); } .c2 .value-icon { background: linear-gradient(135deg, var(--v2), var(--v3)); }
  .c3 { top: 447px; } .c3 .value-title { color: var(--v3); } .c3 .value-icon { background: linear-gradient(135deg, var(--v2), var(--v3)); }
  .c3 .value-body { font-size: 13.5px; line-height: 16px; }
  .c4 { top: 574px; } .c4 .value-title { color: var(--v4); } .c4 .value-icon { background: linear-gradient(135deg, var(--v3), var(--v4)); }
  .c5 { top: 702px; } .c5 .value-title { color: var(--v5); } .c5 .value-icon { background: linear-gradient(135deg, var(--v5), #f3c83a); }
</style>
</head>
<body>
<div class="canvas">

  <div class="icon-row">
    <div class="icon-slot" style="left:296px" role="img" aria-label="Icon: head in profile with a leaf"></div>
    <div class="icon-slot" style="left:440px" role="img" aria-label="Icon: group of people with an arrow"></div>
    <div class="icon-slot" style="left:583px" role="img" aria-label="Icon: light bulb with a copyright sign"></div>
    <div class="icon-slot" style="left:726px" role="img" aria-label="Icon: stopwatch with a tick"></div>
    <div class="icon-slot" style="left:869px" role="img" aria-label="Icon: document with shapes"></div>
  </div>
  <div class="rule"></div>

  <div class="brand">NORVA</div>

  <svg class="connectors" width="1200" height="893" viewBox="0 0 1200 893" aria-hidden="true">
    <g fill="none" stroke-width="3">
      <path d="M0 476 H369 L427 248 H484" stroke="#0d5d7b"/>
      <path d="M0 491 H409 L445 376 H484" stroke="#1383c3"/>
      <path d="M0 504 H484" stroke="#3ec2b3"/>
      <path d="M0 518 H409 L445 632 H484" stroke="#8fe07c"/>
      <path d="M0 531 H369 L427 760 H484" stroke="#f6d945"/>
    </g>
    <path d="M480 240 L492 248 L480 256 Z" fill="#0d5d7b"/>
    <path d="M480 368 L492 376 L480 384 Z" fill="#1383c3"/>
    <path d="M480 496 L492 504 L480 512 Z" fill="#3ec2b3"/>
    <path d="M480 624 L492 632 L480 640 Z" fill="#8fe07c"/>
    <path d="M480 752 L492 760 L480 768 Z" fill="#f6d945"/>
  </svg>

  <div class="values-box"></div>
  <div class="frame-top"></div>
  <div class="frame-bottom"></div>
  <div class="values-title">VALUES</div>
  <div class="values-year">2023</div>
  <div class="year-dashes">
    <span style="background:var(--v1)"></span><span style="background:var(--v2)"></span><span style="background:var(--v3)"></span><span style="background:var(--v4)"></span><span style="background:var(--v5)"></span>
  </div>

  <section class="value-card c1">
    <div class="value-icon" role="img" aria-label="Icon: head in profile with a leaf"></div>
    <div class="value-text">
      <h2 class="value-title">We're open and honest</h2>
      <p class="value-body">Sharing information helps us achieve the best outcomes for<br>our teams and business. We value open, honest, and clear<br>communication.</p>
    </div>
  </section>

  <section class="value-card c2">
    <div class="value-icon" role="img" aria-label="Icon: group of people with an arrow"></div>
    <div class="value-text">
      <h2 class="value-title">We get there faster, together</h2>
      <p class="value-body">Collaboration Is at the heart of what we do, no matter<br>our team.</p>
    </div>
  </section>

  <section class="value-card c3">
    <div class="value-icon" role="img" aria-label="Icon: light bulb with a copyright sign"></div>
    <div class="value-text">
      <h2 class="value-title">We are leaders in copyright<br>and intellectual property</h2>
      <p class="value-body">Leading the conversation in audio-visual copyright compliance<br>and advocating for the protection of intellectual property globally.</p>
    </div>
  </section>

  <section class="value-card c4">
    <div class="value-icon" role="img" aria-label="Icon: stopwatch with a tick"></div>
    <div class="value-text">
      <h2 class="value-title">We get things done</h2>
      <p class="value-body">We grow through capability, focus and hard work. We believe<br>small steps compound to big results.</p>
    </div>
  </section>

  <section class="value-card c5">
    <div class="value-icon" role="img" aria-label="Icon: document with shapes"></div>
    <div class="value-text">
      <h2 class="value-title">Diverse perspectives build better outcomes</h2>
      <p class="value-body">We value diversity, inclusion, respect and trust within our teams.<br>We are building a truly global organisation.</p>
    </div>
  </section>

</div>
</body>
</html>
```